PREVENTING FALLS IN YOUR HOME / MAKING YOUR HOME SAFER

We sell, and install grab bars for only $99 each in the home. Statistics to present: 2.8 million people are treated in emergency rooms annually for falls. 800,000 are hospitalized because of fall injury. 95% of hip fractures are caused by falling. I would like a 1 page marketing piece containing a cartoon like male slipping backwards holding on to shower curtain which is bending curtain rod that cannot support him. Then as a don't and do,same man wisely entering tub using grab bar. Slipping on stairs, trying to grab onto whatever won't hold him would be another scenario.
Included in piece would be above fall statistics separated into bursts, reminder that grab bars can be installed in any room including the garage and a star burst of Only $99, includes bar and installation and

Target Market(s)

over 50 year old market butpredominantly elderly population

Industry/Entity Type

Home Health Care

Font styles to use
Sans Serif

Colors
ec1f27

Requirements
Must have
• instant recognition that a grab bar can prevent serious falls and hip fracture. The cartoon characterization must make instant understanding without reading text
Nice to have
• large print
• concise message
• not a lot of reading to understand
• cartoons in circle with line through don' t circle Ie. no swimming
Should not have
• small print
• congested page

```html
<!DOCTYPE html>
<html lang="en">
<head>
<meta charset="utf-8">
<title>Preventing Falls in Your Home – Grab Bar Flyer</title>
<link rel="stylesheet" href="https://fonts.googleapis.com/css2?family=Anton&family=Roboto:wght@400;500;700;900&display=swap">
<style>
  :root {
    --brand-red: #ec1f27;
    --ink: #111111;
    --paper: #ffffff;
    --stage: #e9e9e9;
    --stat-band: #dcdcdc;
    --divider: #9a9a9a;
  }
  * { margin: 0; padding: 0; box-sizing: border-box; }
  html, body {
    width: 1200px; height: 1200px; overflow: hidden;
    background: var(--stage);
  }
  .flyer {
    position: absolute; left: 155px; top: 24px;
    width: 890px; height: 1152px;
    background: var(--paper);
    overflow: hidden;
    font-family: "Roboto", Arial, sans-serif;
  }
  .headline {
    position: absolute; left: 0; width: 100%;
    text-align: center;
    font-family: "Anton", "Impact", sans-serif;
    line-height: 1; text-transform: uppercase; white-space: nowrap;
  }
  .headline--kicker { top: 44px; font-size: 60px; color: var(--brand-red); letter-spacing: 0.5px; }
  .headline--main { top: 106px; font-size: 76px; color: var(--ink); letter-spacing: 0.5px; }

  .hero-band {
    position: absolute; left: 0; top: 204px; width: 100%; height: 304px;
    background: var(--brand-red);
  }
  .scenes { position: absolute; left: 0; top: 0; width: 890px; height: 620px; }

  .offer-lead {
    position: absolute; left: 75px; top: 592px;
    font-size: 45px; line-height: 44px; color: var(--ink); font-weight: 400;
    text-transform: uppercase; white-space: nowrap;
  }
  .offer-price {
    position: absolute; left: 338px; top: 560px;
    font-family: "Anton", "Impact", sans-serif;
    color: var(--brand-red);
    -webkit-text-stroke: 5px var(--paper);
    paint-order: stroke fill;
    text-shadow: 4px 6px 6px rgba(0,0,0,0.35);
    transform: rotate(-4deg) scaleX(1.2);
    transform-origin: left center;
    line-height: 1; white-space: nowrap;
  }
  .offer-price__currency { font-size: 110px; vertical-align: top; position: relative; top: 28px; }
  .offer-price__amount { font-size: 200px; }
  .offer-note {
    position: absolute; left: 642px; top: 638px;
    font-size: 33px; line-height: 42px; font-weight: 900; color: var(--brand-red);
  }

  .stats-label {
    position: absolute; left: 75px; top: 768px;
    font-size: 22px; font-weight: 700; color: var(--ink); text-transform: uppercase;
  }
  .stats {
    position: absolute; left: 0; top: 797px; width: 100%; height: 140px;
    background: var(--stat-band);
    display: flex;
  }
  .stat { position: relative; padding: 8px 0 0 0; }
  .stat:nth-child(1) { width: 319px; padding-left: 75px; }
  .stat:nth-child(2) { width: 253px; padding-left: 40px; }
  .stat:nth-child(3) { flex: 1; padding-left: 54px; }
  .stat + .stat::before {
    content: ""; position: absolute; left: 0; top: 10px; width: 4px; height: 120px;
    background: linear-gradient(to right, var(--divider), transparent);
  }
  .stat__figure { font-size: 40px; font-weight: 500; color: var(--brand-red); line-height: 46px; }
  .stat__figure sup { font-size: 18px; vertical-align: top; position: relative; top: 4px; }
  .stat__caption {
    margin-top: 10px; font-size: 16.5px; line-height: 21px; color: var(--ink);
    text-transform: uppercase;
  }
  .stat:nth-child(3) .stat__caption { font-size: 15.5px; line-height: 19px; margin-top: 12px; }

  .cta {
    position: absolute; left: 0; width: 100%;
    text-align: center; font-family: "Anton", "Impact", sans-serif;
    line-height: 1; text-transform: uppercase; white-space: nowrap;
  }
  .cta--lead { top: 958px; font-size: 46px; color: var(--brand-red); }
  .cta--main { top: 1004px; font-size: 58px; color: var(--ink); }
  .cta--phone { top: 1060px; font-size: 58px; color: var(--brand-red); }
</style>
</head>
<body>
  <main class="flyer">
    <h1 class="headline headline--kicker">Preventing falls in your home</h1>
    <h2 class="headline headline--main">Making your home safer</h2>

    <div class="hero-band"></div>

    <svg class="scenes" viewBox="0 0 890 620" xmlns="http://www.w3.org/2000/svg">
      <defs>
        <linearGradient id="shower-tone" x1="0" y1="0" x2="0" y2="1">
          <stop offset="0" stop-color="#f6c9cd"/>
          <stop offset="0.72" stop-color="#f0a9af"/>
          <stop offset="0.73" stop-color="#d9353a"/>
          <stop offset="1" stop-color="#c82a30"/>
        </linearGradient>
        <linearGradient id="stair-tone" x1="0" y1="0" x2="0" y2="1">
          <stop offset="0" stop-color="#86c24a"/>
          <stop offset="0.66" stop-color="#6fac3a"/>
          <stop offset="0.67" stop-color="#c9393d"/>
          <stop offset="1" stop-color="#8f2226"/>
        </linearGradient>
      </defs>
      <circle cx="318" cy="327" r="140" fill="url(#shower-tone)" stroke="#ffffff" stroke-width="5"
              role="img" aria-label="Illustration: cartoon man slipping backwards in a tiled shower"/>
      <circle cx="120" cy="464" r="96" fill="url(#stair-tone)" stroke="#ffffff" stroke-width="5"
              role="img" aria-label="Illustration: cartoon man falling on the stairs"/>
      <circle cx="685" cy="424" r="185" fill="url(#shower-tone)" stroke="#ffffff" stroke-width="5"
              role="img" aria-label="Illustration: cartoon man showering safely while holding a grab bar"/>
      <circle cx="475" cy="472" r="104" fill="url(#stair-tone)" stroke="#ffffff" stroke-width="5"
              role="img" aria-label="Illustration: cartoon man climbing stairs holding a handrail"/>
    </svg>

    <p class="offer-lead">Install<br>grab bars<br>for only</p>
    <p class="offer-price"><span class="offer-price__currency">$</span><span class="offer-price__amount">99</span></p>
    <p class="offer-note">each in<br>the home</p>

    <p class="stats-label">Statistics to present</p>
    <section class="stats">
      <div class="stat">
        <p class="stat__figure">2.8 million</p>
        <p class="stat__caption">People are treated in<br>emergency rooms<br>annually for falls</p>
      </div>
      <div class="stat">
        <p class="stat__figure">800,000</p>
        <p class="stat__caption">Are hospitalized<br>because of fall<br>injury.</p>
      </div>
      <div class="stat">
        <p class="stat__figure">95<sup>%</sup></p>
        <p class="stat__caption">Of hip fractures<br>are caused by<br>falling</p>
      </div>
    </section>

    <p class="cta cta--lead">Call us now and</p>
    <p class="cta cta--main">Making your home safer</p>
    <p class="cta cta--phone">555 014 2368</p>
  </main>
</body>
</html>
```